Bright Meadow Dental - Stationary
Business Cards, Letterhead, & Envelope
Project: Bright Meadow Dental - Stationary
Bright Meadow Dental - Stationary - Health
Creative Brief
Professional
Leland Fisk, D.D.S.
3847 W Thornbury Ln, Suite 2 Gladstone, MO 64102
BrightMeadowDental@mailbox-example.com
www.BrightMeadowDental-example.com
We're a fun office and want people to expect great cosmetic work and accommodations for families. We don't need a "blow your mind" presentation, just something classy.

```html
<!DOCTYPE html>
<html lang="en">
<head>
<meta charset="utf-8">
<title>Bright Meadow Dental – Business Cards</title>
<link rel="stylesheet" href="https://fonts.googleapis.com/css2?family=Arimo:wght@400;700&family=Lora:ital,wght@1,700&display=swap">
<style>
  :root {
    --bg: #ece8e3;
    --brand-blue: #1f68b3;
    --brand-deep: #0f4f93;
    --brand-light: #3a86cf;
    --ink: #333a42;
    --muted: #7d858e;
    --card-white: #ffffff;
    --card-grey: #e9ebee;
    --swoosh-grey: #c9ced4;
  }
  * { box-sizing: border-box; margin: 0; padding: 0; }
  html, body { width: 1200px; height: 791px; overflow: hidden; }
  body { background: var(--bg); position: relative; font-family: "Arimo", Arial, sans-serif; }

  .card {
    position: absolute;
    width: 466px;
    height: 268px;
    border-radius: 12px;
    overflow: hidden;
    box-shadow: 0 6px 16px rgba(0,0,0,.22);
  }
  .card--contact { left: 372px; top: 92px; background: var(--card-white); }
  .card--blue    { left: 132px; top: 398px; background: radial-gradient(ellipse at 45% 40%, var(--brand-light), var(--brand-deep) 80%); }
  .card--white   { left: 618px; top: 398px; background: radial-gradient(ellipse at 50% 40%, #ffffff, var(--card-grey) 85%); }

  .swoosh { position: absolute; left: 0; bottom: 0; width: 100%; height: 90px; }

  .brand { position: absolute; display: flex; flex-direction: column; }
  .brand__row { display: flex; align-items: center; gap: 10px; }
  .brand__mark { width: 18px; height: 18px; border-radius: 50%; flex: none; }
  .brand__name {
    font-family: "Arimo", Arial, sans-serif;
    font-weight: 400;
    letter-spacing: 1px;
    line-height: 1.05;
    text-transform: uppercase;
    white-space: nowrap;
  }
  .brand__tagline {
    font-family: "Lora", Georgia, serif;
    font-style: italic;
    font-weight: 700;
    margin-top: 6px;
    white-space: nowrap;
  }

  .card--contact .brand { left: 20px; top: 72px; }
  .card--contact .brand__name { font-size: 18px; color: var(--brand-blue); }
  .card--contact .brand__mark { width: 14px; height: 14px; background: var(--brand-blue); }
  .card--contact .brand__tagline { font-size: 9.5px; color: var(--brand-blue); }

  .divider { position: absolute; left: 240px; top: 60px; width: 2px; height: 80px; background: var(--brand-blue); }

  .contact { position: absolute; left: 252px; top: 50px; color: var(--ink); }
  .contact__name { font-size: 18px; color: var(--brand-blue); font-weight: 400; margin-bottom: 10px; white-space: nowrap; }
  .contact__line { font-size: 9px; line-height: 12px; white-space: nowrap; }
  .contact__list { list-style: none; margin-top: 3px; }
  .contact__list li { font-size: 9px; line-height: 13px; display: flex; align-items: center; gap: 5px; white-space: nowrap; }
  .contact__list svg { width: 7px; height: 7px; flex: none; }

  .web { position: absolute; font-size: 10px; letter-spacing: .3px; white-space: nowrap; }
  .card--contact .web { right: 22px; bottom: 12px; color: #ffffff; }

  .card--blue .brand, .card--white .brand { left: 82px; top: 92px; }
  .card--blue .brand__name, .card--white .brand__name { font-size: 26px; }
  .card--blue .brand__mark, .card--white .brand__mark { width: 20px; height: 20px; }
  .card--blue .brand__name { color: #ffffff; }
  .card--blue .brand__mark { background: #ffffff; }
  .card--blue .brand__tagline { color: #ffffff; font-size: 12.5px; }
  .card--white .brand__name { color: var(--brand-blue); }
  .card--white .brand__mark { background: var(--brand-blue); }
  .card--white .brand__tagline { color: var(--brand-blue); font-size: 12.5px; }

  .card--blue .web, .card--white .web { left: 0; right: 0; bottom: 14px; text-align: center; }
  .card--blue .web { color: #ffffff; }
  .card--white .web { color: var(--ink); }
</style>
</head>
<body>

  <section class="card card--contact" aria-label="Business card, contact side">
    <svg class="swoosh" viewBox="0 0 466 90" preserveAspectRatio="none" aria-hidden="true">
      <path d="M0 40 C150 20 300 30 466 50 L466 90 L0 90 Z" fill="var(--swoosh-grey)"/>
      <path d="M0 52 C160 30 310 40 466 58 L466 90 L0 90 Z" fill="#ffffff"/>
      <path d="M0 60 C170 42 320 50 466 62 L466 90 L0 90 Z" fill="var(--brand-light)"/>
      <path d="M0 68 C180 52 330 58 466 66 L466 90 L0 90 Z" fill="var(--brand-blue)"/>
    </svg>

    <div class="brand">
      <div class="brand__row">
        <span class="brand__name">Bright Meadow<br>Dental</span>
        <span class="brand__mark" aria-hidden="true"></span>
      </div>
      <span class="brand__tagline">Cosmetic and Family Dentistry</span>
    </div>

    <div class="divider" aria-hidden="true"></div>

    <div class="contact">
      <h1 class="contact__name">Leland Fisk, D.D.S</h1>
      <p class="contact__line">3847 W Thornbury Ln, Suite 2</p>
      <p class="contact__line">Larkfield, NE 68102</p>
      <ul class="contact__list">
        <li><svg viewBox="0 0 8 8"><circle cx="4" cy="4" r="4" fill="var(--muted)"/></svg>4025550142</li>
        <li><svg viewBox="0 0 8 8"><circle cx="4" cy="4" r="4" fill="var(--muted)"/></svg>4025550187</li>
        <li><svg viewBox="0 0 8 8"><circle cx="4" cy="4" r="4" fill="var(--muted)"/></svg>BrightMeadowDental@mailbox-example.com</li>
      </ul>
    </div>

    <p class="web">www.BrightMeadowDental-example.com</p>
  </section>

  <section class="card card--blue" aria-label="Business card, blue logo side">
    <div class="brand">
      <div class="brand__row">
        <span class="brand__name">Bright Meadow<br>Dental</span>
        <span class="brand__mark" aria-hidden="true"></span>
      </div>
      <span class="brand__tagline">Cosmetic and Family Dentistry</span>
    </div>
    <p class="web">www.BrightMeadowDental-example.com</p>
  </section>

  <section class="card card--white" aria-label="Business card, white logo side">
    <div class="brand">
      <div class="brand__row">
        <span class="brand__name">Bright Meadow<br>Dental</span>
        <span class="brand__mark" aria-hidden="true"></span>
      </div>
      <span class="brand__tagline">Cosmetic and Family Dentistry</span>
    </div>
    <p class="web">www.BrightMeadowDental-example.com</p>
  </section>

</body>
</html>
```